Create a Big Data Website that is professional but has a creative flare to it.

I am after a modern business design for a company in the Big Data space however it still needs to have a wow value and something stand out from other corporate websites.
My competitors websites are to give you and idea of content:
www.fendralux.com
www.vornuby.com
www.quillmerq4.com.au
www.tessovant.com
I have uploaded my company Logo so you can use that to make sure it matches your theme.

Target Market(s)

Banks, Insurance Companies, Government, Gas and Energy Companies and Food Manufacturing.

Industry/Entity Type

Consulting

Number of Pages Required

5+ page

Colors

Designer to choose colors to be used in the design.

Requirements
Must have
• Images, Diagrams around Big Data. Usage of information or graphs from sources like Pellwick are fine to use.
Nice to have
• Interactive design use mouse overs, change in text, highlighting information for clear focus.
Should not have
• Cluttered Pages of Informaiton

```html
<!DOCTYPE html>
<html lang="en">
<head>
<meta charset="utf-8">
<title>Veridane Consulting Services – Big Data Analytics Solutions</title>
<link rel="stylesheet" href="https://fonts.googleapis.com/css2?family=Open+Sans:wght@300;400;600;700&family=Roboto+Condensed:wght@400&display=swap">
<style>
:root{
  --navy-deep:#050b1c;
  --hero-blue:#0c2a5c;
  --band-blue:#1b6fc2;
  --band-cyan:#3fe1ea;
  --section-blue:#2b4676;
  --value-blue:#143e88;
  --accent:#2fa3e6;
  --ink-dark:#2a3d6a;
  --card-dark:#071022;
  --partner-grey:#cfcfd1;
  --footer:#252c3c;
  --footer-bar:#0b1424;
  --white:#ffffff;
  --muted:#9aa3b5;
  --footer-brand:#8b8676;
}
*{box-sizing:border-box;margin:0;padding:0}
html,body{width:672px;height:1200px;overflow:hidden}
body{font-family:"Open Sans",sans-serif;color:var(--white);background:var(--navy-deep);position:relative}
.hero{position:absolute;left:0;top:0;width:672px;height:288px;background:radial-gradient(ellipse at 55% 40%,#0f3c7c 0%,var(--hero-blue) 45%,var(--navy-deep) 100%)}
.brand{display:flex;align-items:center;gap:8px}
.hero .brand{position:absolute;left:58px;top:24px}
.brand-mark{width:22px;height:22px;background:var(--accent);flex:none}
.brand-name{font-size:21px;font-weight:700;line-height:1;display:block}
.brand-sub{font-size:7px;letter-spacing:1px;color:var(--accent);font-weight:600;display:block;margin-top:2px}
.nav{position:absolute;top:34px;left:311px;display:flex;font-size:8.5px}
.nav a{color:var(--white);text-decoration:none;margin-right:20px}
.hero-photo{position:absolute;left:58px;top:80px;width:345px;height:208px;background:linear-gradient(180deg,rgba(230,235,245,0) 0%,rgba(220,228,240,.55) 40%,rgba(235,240,248,.85) 100%);border-radius:60px 60px 0 0}
.hero-title{position:absolute;left:311px;top:112px;border-left:1px solid rgba(255,255,255,.6);padding-left:7px;font-weight:300;font-size:30px;line-height:36px}
.bands{position:absolute;top:288px;left:0;width:672px;height:108px;display:flex}
.band{width:336px;height:108px;text-align:center}
.band-bi{background:linear-gradient(90deg,#1a5ea8,var(--band-blue))}
.band-bi h2{font-size:17px;font-weight:700;margin-top:19px}
.band-bi p{font-size:8px;line-height:10.5px;width:200px;margin:3px auto 0}
.band-edge{background:linear-gradient(90deg,var(--band-cyan),#36cfe0)}
.band-edge h2{color:var(--ink-dark);font-size:19px;line-height:24px;font-weight:700;margin-top:22px}
.band-edge p{color:#2b6b8c;font-size:8px;line-height:10px;width:190px;margin:3px auto 0}
.services{position:absolute;top:396px;left:0;width:672px;height:303px;background:var(--section-blue)}
.service{position:absolute;top:34px;width:180px;height:262px}
.service-media{display:flex;height:122px}
.service-icon{width:43px;background:var(--card-dark);display:flex;align-items:center;justify-content:center}
.service-photo{flex:1}
.service h3{font-size:17.5px;line-height:21px;font-weight:600;color:var(--accent);margin:6px 0 3px 42px;white-space:nowrap}
.service p{font-size:8.2px;line-height:10.2px;margin-left:42px;width:138px}
.service a{position:absolute;left:42px;font-size:8.5px;color:var(--accent);text-decoration:none}
.value{position:absolute;top:699px;left:0;width:672px;height:242px;background:linear-gradient(135deg,#123a80 0%,var(--value-blue) 50%,#1c4a9a 100%)}
.value h2{position:absolute;left:58px;top:20px;font-size:20px;font-weight:600;color:var(--accent);display:flex;align-items:center;gap:4px}
.value-art{position:absolute;left:110px;top:60px;width:175px;height:115px;border-radius:60px 60px 20px 20px;background:linear-gradient(180deg,#3aa8e6 0%,#8fb6d6 50%,#2a2f3a 100%)}
.value p{position:absolute;left:100px;top:191px;width:200px;text-align:center;font-size:8.3px;line-height:10.5px;color:var(--accent)}
.partners{position:absolute;top:941px;left:0;width:672px;height:64px;background:var(--partner-grey);display:flex;align-items:center}
.partners h2{margin-left:58px;color:var(--ink-dark);font-size:16px;line-height:17px;font-weight:700;display:flex;gap:4px;width:120px}
.partner-list{display:flex;gap:26px;margin-left:4px}
.partner{font-size:13px;font-weight:600;color:#3b4a5c}
.footer{position:absolute;top:1005px;left:0;width:672px;height:154px;background:var(--footer)}
.footer h4{font-size:8.5px;letter-spacing:1.6px;font-weight:600;margin-bottom:10px}
.col{position:absolute;top:45px}
.col p,.col li{font-size:6.6px;line-height:9px;color:var(--muted)}
.col ul{list-style:none}
.col li{margin-bottom:5.5px}
.col li::before{content:"▸ ";color:var(--muted)}
.footer-brand{position:absolute;left:473px;top:36px}
.footer-brand .brand-mark{background:var(--footer-brand)}
.footer-brand .brand-name{color:var(--footer-brand)}
.footer-brand .brand-sub{color:var(--footer-brand)}
.footer-brand address{font-style:normal;font-size:6.3px;line-height:8.4px;color:#d8dbe2;margin:10px 0 0 39px}
.footer-brand address span{display:block;margin-top:6px}
.copyright{position:absolute;top:1159px;left:0;width:672px;height:41px;background:var(--footer-bar);text-align:center;font-family:"Roboto Condensed",sans-serif;font-size:10px;line-height:41px;color:var(--accent)}
</style>
</head>
<body>
<header class="hero">
  <div class="brand"><span class="brand-mark"></span><div><span class="brand-name">veridane</span><span class="brand-sub">CONSULTING SERVICES</span></div></div>
  <nav class="nav"><a href="#">Home</a><a href="#">About us</a><a href="#">Partners</a><a href="#">Big Data Solutions</a><a href="#">Blog</a><a href="#">Contact</a></nav>
  <div class="hero-photo" role="img" aria-label="Smiling consultant in white shirt and tie presenting with open hand"></div>
  <h1 class="hero-title">Big Data Analytics<br>SOLUTIONS</h1>
</header>

<section class="bands">
  <div class="band band-bi">
    <h2>BUSINESS INTELLIGENCE</h2>
    <p>Understand your business, your customers and your market with sophisticated query, reporting and data exploration capabilities. Quillmerq4 can provide skilled consultants to work with your team, or a complete solution end-to-end.</p>
  </div>
  <div class="band band-edge">
    <h2>CUTTING-EDGE<br>ANALYTICS SOLUTIONS</h2>
    <p>Maximise organisational performance using the power of data and analytics</p>
  </div>
</section>

<section class="services">
  <article class="service" style="left:58px">
    <div class="service-media">
      <div class="service-icon"><svg width="30" height="26" viewBox="0 0 30 26"><rect x="1" y="1" width="28" height="24" rx="3" fill="none" stroke="#fff" stroke-width="2"/><rect x="7" y="13" width="3" height="8" fill="#fff"/><rect x="12" y="9" width="3" height="12" fill="#fff"/><rect x="17" y="6" width="3" height="15" fill="#fff"/><rect x="22" y="11" width="3" height="10" fill="#fff"/></svg></div>
      <div class="service-photo" role="img" aria-label="Consultant drawing growth charts on a glass board" style="background:linear-gradient(135deg,#f4f5f7,#c9cdd3)"></div>
    </div>
    <h3>Advanced<br>Analytics</h3>
    <p>Forecast performance, understand risk and build sophisticated business insights using statistical modelling, machine learning and data mining techniques.</p>
    <a href="#" style="top:236px">Read more</a>
  </article>
  <article class="service" style="left:246px">
    <div class="service-media">
      <div class="service-icon"><svg width="30" height="30" viewBox="0 0 30 30"><circle cx="11" cy="13" r="6" fill="none" stroke="#fff" stroke-width="4" stroke-dasharray="3 2"/><circle cx="11" cy="13" r="2" fill="#fff"/><circle cx="22" cy="8" r="4" fill="none" stroke="#fff" stroke-width="3" stroke-dasharray="2 1.5"/><circle cx="21" cy="22" r="4" fill="none" stroke="#fff" stroke-width="3" stroke-dasharray="2 1.5"/></svg></div>
      <div class="service-photo" role="img" aria-label="Analyst at a desk working on data dashboards" style="background:linear-gradient(135deg,#eef0f3,#b9c3cf)"></div>
    </div>
    <h3>Data Integration</h3>
    <p>Focus on high-value analytical tasks using integrated, quality-tested data. Swiftlane, our data integration methodology and accelerator, delivers flexible, easy maintained, best-practice integration using automated, model-driven techniques in record time.</p>
    <a href="#" style="top:247px">Read more</a>
  </article>
  <article class="service" style="left:435px">
    <div class="service-media">
      <div class="service-icon"><svg width="32" height="22" viewBox="0 0 32 22"><path d="M8 21a7 7 0 0 1-1-13.9A9 9 0 0 1 24 6a7.5 7.5 0 0 1 0 15z" fill="#fff"/><path d="M16 8l-5 5h3v4h4v-4h3z" fill="var(--card-dark)"/></svg></div>
      <div class="service-photo" role="img" aria-label="Engineer with laptop in a server room aisle" style="background:linear-gradient(135deg,#3c4a55,#8a9aa5)"></div>
    </div>
    <h3>Data warehousing</h3>
    <p>Clean, high-quality, well-integrated data is the foundation of your analytics and reporting programme. Our consultants have the skills and experience to successfully design, deliver, enhance and support your data warehouse.</p>
    <a href="#" style="top:247px">Read more</a>
  </article>
</section>

<section class="value">
  <h2><svg width="18" height="16" viewBox="0 0 18 16"><path d="M1 1l7 7-7 7M9 1l7 7-7 7" fill="none" stroke="var(--accent)" stroke-width="2"/></svg>Create Value From Data</h2>
  <div class="value-art" role="img" aria-label="Server racks inside a blue cloud shape"></div>
  <p>Achieve scalability, agility and cost-benefits using cloud-based analytics, data warehousing and data integration deployments.</p>
</section>

<section class="partners">
  <h2><svg width="18" height="16" viewBox="0 0 18 16"><path d="M1 1l7 7-7 7M9 1l7 7-7 7" fill="none" stroke="var(--ink-dark)" stroke-width="2"/></svg><span>Meet our<br>partners</span></h2>
  <div class="partner-list">
    <span class="partner">Orvanta</span><span class="partner">Clemmora</span><span class="partner">Nesspire</span><span class="partner">Dalvistra</span><span class="partner">Torquell</span>
  </div>
</section>

<footer class="footer">
  <div class="col" style="left:72px;width:150px">
    <h4>ABOUT US</h4>
    <p>Vitae adipiscing turpis. Aenean ligula nibh in, molestie id viverra a, dapibus at dolor. Aenean ligula nibh in, molestie id viverra a, dapibus at dolor.molestie id viverra a, dapibus.</p>
  </div>
  <div class="col" style="left:267px">
    <h4>OUR OFFER</h4>
    <ul><li>Aenean sollicitudin orem qui at dolor</li><li>Duis sed odio sit amet viverra a nibh</li><li>Morbi accumsan ipsum velit adipiscing</li></ul>
  </div>
  <div class="footer-brand">
    <div class="brand"><span class="brand-mark"></span><div><span class="brand-name">veridane</span><span class="brand-sub">CONSULTING SERVICES</span></div></div>
    <address>Tel: +61 200 000 417<br>Level 4, 212 Harlow Street,<br>Melbourne, VIC, 3000<br>Australia<span>info@veridane.com</span></address>
  </div>
</footer>
<div class="copyright">© 2017 Veridane - All rights reserved.</div>
</body>
</html>
```